Business Card Design Project

Use our current logo. Clean design.

Industry/Entity Type

Business

Requirements
Must have
• Marisela DUBRANCQ
M. Law
Managing Partner

Alpenvorsa AG
Kornhalmweg 214
CH-3097 Liebefeld

M. +41 79 412 56 27
T. +41 31 928 44 10
F. +41 31 928 44 19

m.dubrancq@alpenvorsa-example.com
www.alpenvorsa-example.com

```html
<!DOCTYPE html>
<html lang="en">
<head>
<meta charset="utf-8">
<title>Alpenvorsa AG – Stationery</title>
<link rel="stylesheet" href="https://fonts.googleapis.com/css2?family=Questrial&display=swap">
<style>
  :root {
    --backdrop: #f2f2f2;
    --paper: #ffffff;
    --brand-red: #e41b23;
    --ink: #111111;
  }
  html, body {
    margin: 0;
    padding: 0;
    width: 1200px;
    height: 899px;
    overflow: hidden;
    background: var(--backdrop);
    font-family: "Questrial", "Century Gothic", sans-serif;
    color: var(--ink);
  }
  .stage { position: relative; width: 1200px; height: 899px; }
  .sheet {
    position: absolute;
    background: var(--paper);
    overflow: hidden;
  }
  .sheet svg.swoosh { position: absolute; left: 0; top: 0; }
  .letterhead { left: 150px; top: 159px; width: 450px; height: 581px; }
  .envelope { left: 647px; top: 277px; width: 400px; height: 189px; }
  .card { left: 647px; top: 480px; width: 403px; height: 190px; }

  .brand-name {
    position: absolute;
    letter-spacing: 0.5px;
    color: var(--ink);
    white-space: nowrap;
  }
  .letterhead .brand-name { left: 300px; top: 50px; font-size: 17px; }
  .card .brand-name { left: 22px; top: 34px; font-size: 11px; }

  .contact { position: absolute; white-space: nowrap; }
  .accent { color: var(--brand-red); }
  .small { font-size: 6px; }

  .letterhead .contact-block { left: 49px; top: 514px; width: 262px; font-size: 7.5px; line-height: 14px; }
  .letterhead .contact-block .company { font-size: 11px; margin-right: 3px; }
  .letterhead .contact-block .row-web { display: flex; justify-content: space-between; gap: 12px; }

  .envelope .contact-line { left: 30px; top: 167px; font-size: 5.5px; }
  .envelope .contact-line .company { font-size: 8px; }
  .envelope .contact-line .phones { margin-left: 18px; }

  .card .person { left: 33px; top: 152px; font-size: 7.5px; }
  .card .person .title { margin-left: 6px; }
  .card .contact-line { left: 33px; top: 167px; font-size: 7.5px; }
  .card .contact-line .accent { margin-left: 8px; }
</style>
</head>
<body>
<main class="stage">

  <section class="sheet letterhead" aria-label="Letterhead">
    <svg class="swoosh" width="450" height="581" viewBox="0 0 450 581" aria-hidden="true">
      <defs>
        <linearGradient id="lh-grey-top" x1="0" y1="1" x2="1" y2="0">
          <stop offset="0" stop-color="#444"/><stop offset="0.6" stop-color="#bbb"/><stop offset="1" stop-color="#eee"/>
        </linearGradient>
        <linearGradient id="lh-grey-bottom" x1="0" y1="0" x2="1" y2="0">
          <stop offset="0" stop-color="#f2f2f2"/><stop offset="0.6" stop-color="#bdbdbd"/><stop offset="1" stop-color="#555"/>
        </linearGradient>
      </defs>
      <path d="M0,0 H90 Q40,12 0,36 Z" fill="var(--ink)"/>
      <path d="M0,44 Q90,8 250,0 L272,0 Q80,20 0,90 Z" fill="var(--brand-red)"/>
      <path d="M0,90 Q80,20 272,0 Q90,28 0,102 Z" fill="url(#lh-grey-top)"/>
      <path d="M270,581 Q380,560 450,512 L450,546 Q380,574 300,581 Z" fill="url(#lh-grey-bottom)"/>
      <path d="M352,581 Q418,572 450,556 V581 Z" fill="var(--brand-red)"/>
    </svg>
    <div class="brand-name">ALPENVORSA</div>
    <div class="contact contact-block">
      <div><span class="company">Alpenvorsa AG</span> <span class="accent">Kornhalmweg 214</span> <span class="small">CH-3097 Liebefeld</span></div>
      <div><span class="accent">M. +41 79 412 56 27</span>&nbsp; T. +41 31 928 44 10&nbsp; <span class="accent">F. +41 31 928 44 19</span></div>
      <div class="row-web"><span>www.alpenvorsa-example.com</span><span class="accent">m.dubrancq@alpenvorsa-example.com</span></div>
    </div>
  </section>

  <section class="sheet envelope" aria-label="Envelope">
    <svg class="swoosh" width="400" height="189" viewBox="0 0 400 189" aria-hidden="true">
      <path d="M2,3 Q2,0 6,0 H394 Q398,0 398,3 L388,47 Q387,52 382,52 H18 Q13,52 12,47 Z" fill="var(--brand-red)"/>
    </svg>
    <div class="contact contact-line">
      <span class="company">Alpenvorsa AG</span> <span class="accent">Kornhalmweg 214</span> CH-3097 Liebefeld
      <span class="phones"><span class="accent">M. +41 79 412 56 27</span> T. +41 31 928 44 10 <span class="accent">F. +41 31 928 44 19</span></span>
    </div>
  </section>

  <section class="sheet card" aria-label="Compliment card">
    <svg class="swoosh" width="403" height="190" viewBox="0 0 403 190" aria-hidden="true">
      <defs>
        <linearGradient id="cd-grey" x1="0" y1="0" x2="1" y2="0">
          <stop offset="0" stop-color="#f2f2f2"/><stop offset="0.6" stop-color="#bdbdbd"/><stop offset="1" stop-color="#555"/>
        </linearGradient>
      </defs>
      <path d="M0,0 H40 Q18,5 0,12 Z" fill="var(--ink)"/>
      <path d="M0,18 Q40,4 70,0 H82 Q30,10 0,32 Z" fill="var(--brand-red)"/>
      <path d="M270,190 Q350,178 403,140 V165 Q350,184 300,190 Z" fill="url(#cd-grey)"/>
      <path d="M340,190 Q380,182 403,174 V190 Z" fill="var(--brand-red)"/>
    </svg>
    <div class="brand-name">ALPENVORSA</div>
    <div class="contact person">Marisela DUBRANCQ, M. Law<span class="title accent">Managing Partner</span></div>
    <div class="contact contact-line">
      m.dubrancq@alpenvorsa-example.com<span class="accent">www.alpenvorsa-example.com</span>
    </div>
  </section>

</main>
</body>
</html>
```